Real Estate Website Design Needed of IDX Intergration

I need a 'Lead Capture' Website the will be use for marketing to site visitors looking to buy a home/land in Central Florida (Greater Orlando, Florida), United States.

Competitor Websites that I like;

Halvorsenhomes.com (Like the Most)
TheDraplinCircle.com (Good One-Line Property Search Form)
TheMarlows.com (Good 'High-End' Look)
FreshDoorKeyHaven.com (Good Property Search Form)

The project title should be; "Real Estate Website Design Needed FOR IDX Intergration"

Target Market(s)

Consumers looking to purchase homes or land in the Central Florida, United States

Industry/Entity Type

Real Estate

Logo Text

Pine Gate Porch Realty or PineGatePorchRealty or Pine GatePorch Realty

Number of Pages Required

1 page

Font styles to use
Serif
Sans Serif

Colors

Designer to choose colors to be used in the design.

Requirements
Must have
• Our Team Name: 'PineGatePorchRealty Real Estate Team' is an important part of the design. Our Contact information needs to be apart of the design; Phone Number: (555) 614-2970 Email: ReachOut@PineGatePorchRealty.example MOST IMPORTANTLY we must have Opt-In Buttons/Contact Form 'above the break' of the site, see a great example at Halvorsenhomes.com
• Other Needs;
• -Search Engine Friendly Design
• -The attached must be present in the footnote of the design

```html
<!DOCTYPE html>
<html lang="en">
<head>
<meta charset="utf-8">
<title>Pine Gate Porch Realty – Real Estate Team</title>
<link href="https://fonts.googleapis.com/css2?family=Lora:ital,wght@0,400;0,700;1,400&family=Open+Sans:wght@400;600;700&display=swap" rel="stylesheet">
<style>
:root{
  --navy:#1c4a70;
  --navy-deep:#174268;
  --heading:#1d4a6f;
  --blue:#2073c1;
  --orange:#f7941d;
  --text:#555;
  --muted:#8a8a8a;
  --soft:#f3f3f3;
  --line:#dcdcdc;
  --footer:#2b2b2b;
  --serif:'Lora',Georgia,serif;
  --sans:'Open Sans',Arial,sans-serif;
}
*{box-sizing:border-box;margin:0;padding:0}
html,body{width:1200px;height:3542px;overflow:hidden}
body{position:relative;background:#fff;font-family:var(--sans);color:var(--text)}
a{color:inherit;text-decoration:none}
h1,h2,h3{font-weight:400}
.abs{position:absolute}

/* header */
.site-header{position:absolute;left:0;top:0;width:1200px;height:135px}
.brand-mark{left:132px;top:34px;width:44px;height:66px;border:4px solid #a7a7a7;border-radius:3px}
.brand-name{left:188px;top:24px;font-family:var(--serif);font-size:33px;color:var(--navy)}
.brand-rule{left:188px;top:76px;width:287px;height:1px;background:#9aa}
.brand-tag{left:188px;top:87px;font-family:var(--serif);font-size:15px;color:#333;letter-spacing:.3px}
.header-contact{right:133px;top:40px;text-align:right;font-family:var(--serif);font-size:15px;color:#333;line-height:29px}
.header-contact svg{vertical-align:-2px;margin-right:5px}

/* nav */
.main-nav{top:135px;left:0;width:1200px;height:44px;background:var(--navy);display:flex;justify-content:space-between;align-items:center;padding:0 133px 0 132px}
.main-nav a{font-family:var(--serif);font-size:14px;color:#fff;text-transform:uppercase}
.main-nav a.active{text-decoration:underline}

/* hero */
.hero{top:179px;left:0;width:1200px;height:434px;background:linear-gradient(100deg,#233248 0%,#4a4a48 30%,#7a5a3c 48%,#2d3f5c 70%,#3b4e6b 100%)}
.hero-title{left:131px;top:170px;font-family:var(--serif);font-weight:700;font-size:30px;color:#fff;text-shadow:0 2px 4px rgba(0,0,0,.6)}
.btn{display:flex;align-items:center;justify-content:center;font-family:var(--serif);font-size:16px}
.btn-buy{left:131px;top:217px;width:145px;height:42px;background:var(--navy);color:#fff}
.btn-sell{left:284px;top:217px;width:144px;height:42px;background:#fff;color:var(--navy)}
.hero-arrow{top:208px}

.search-panel{left:713px;top:77px;width:355px;height:357px;background:#fff}
.search-head{height:47px;background:var(--blue);color:#fff;font-family:var(--sans);font-weight:700;font-size:20px;display:flex;align-items:center;justify-content:center;letter-spacing:.3px}
.field{position:absolute;height:37px;border:1px solid #cfcfcf;font-size:12px;color:#888;display:flex;align-items:center;padding-left:12px}
.field .caret{position:absolute;right:0;top:0;width:39px;height:35px;border-left:1px solid #cfcfcf;display:flex;align-items:center;justify-content:center}
.label{position:absolute;font-size:11px;font-weight:600;color:#444}
.search-btn{left:20px;top:299px;width:100px;height:43px;background:var(--orange);color:#fff;font-weight:700;font-size:15px;display:flex;align-items:center;justify-content:center}
.adv-link{left:137px;top:313px;font-size:12px;color:#666;text-decoration:underline;font-weight:600}

/* section titles */
.section-title{position:absolute;left:0;width:1200px;text-align:center;font-family:var(--serif);font-weight:400;font-size:33px;color:var(--heading);text-transform:uppercase}

/* welcome */
.welcome-text{left:132px;top:733px;width:936px;text-align:center;font-size:11.2px;line-height:20px;color:#555}
.rule{position:absolute;left:0;width:1200px;height:1px;background:var(--line)}

/* listings */
.mini-arrow{position:absolute;top:969px;width:23px;height:21px;border:1px solid #bbb;display:flex;align-items:center;justify-content:center}
.listing{position:absolute;top:1017px;width:298px}
.photo{width:100%}
.listing .photo{height:207px}
.listing h3{margin-top:20px;font-family:var(--serif);font-weight:400;font-size:19px;color:var(--heading)}
.listing .addr{font-family:var(--serif);font-size:13px;color:#333;margin-top:2px}
.listing .price{font-family:var(--serif);font-size:13px;color:#333;margin-top:9px}
.listing .price b{font-weight:400;font-size:18px}

/* sell */
.sell-band{top:1398px;left:0;width:1200px;height:400px;background:var(--navy-deep)}
.sell-title{left:132px;top:60px;font-family:var(--serif);font-weight:400;font-size:33px;color:#fff}
.sell-text{left:132px;top:107px;width:445px;font-size:11.4px;line-height:20px;color:#e8eef5}
.btn-read{left:132px;top:294px;width:97px;height:41px;border:1px solid #cfd9e4;color:#fff;font-size:11.5px;display:flex;align-items:center;justify-content:center}
.sell-photo{left:628px;top:67px;width:440px;height:268px;background:linear-gradient(120deg,#e9e9ea 0%,#d8d2cd 40%,#c94a52 55%,#2c3a55 80%,#e4e6ea 100%)}

/* testimonials */
.testi{top:1798px;left:0;width:1200px;height:327px;background:var(--soft)}
.quote{left:132px;top:130px;width:936px;text-align:center;font-family:var(--serif);font-style:italic;font-size:18px;line-height:27px;color:#666}
.author{left:0;top:221px;width:1200px;text-align:center;font-family:var(--serif);font-size:17px;color:#333}

/* blog */
.blog-title{left:131px;top:2196px;font-family:var(--serif);font-weight:400;font-size:33px;color:var(--heading)}
.view-all{right:133px;top:2208px;font-family:var(--serif);font-size:17px;color:var(--heading);text-decoration:underline}
.post{position:absolute;top:2261px;width:298px;height:415px;background:var(--soft)}
.post .photo{height:191px}
.post-body{padding:21px 19px}
.post h3{font-weight:400;font-size:16px;line-height:21px;color:#333}
.post .date{font-size:9.5px;color:#777;margin-top:12px}
.post p{font-size:10px;line-height:16px;color:#888;margin-top:12px}
.post .more{display:inline-block;margin-top:9px;font-size:10px;color:#333;text-decoration:underline;font-weight:600}

/* contact */
.contact-box{left:132px;top:2885px;width:468px;height:279px;background:var(--soft)}
.contact-line{position:absolute;left:33px;font-size:16px;color:#666;display:flex;align-items:center;gap:12px}
.social-ring{position:absolute;top:184px;width:42px;height:42px;border:1px solid #c9c9c9;border-radius:50%}
.map{left:600px;top:2885px;width:468px;height:279px;background:linear-gradient(135deg,#ececec,#dedede 60%,#e8e8e8)}

/* footer */
.site-footer{top:3244px;left:0;width:1200px;height:298px;background:var(--footer)}
.legal{left:132px;width:936px;font-size:10.3px;line-height:19px;color:#a9a9a9}
.footer-rule{left:132px;top:194px;width:936px;height:1px;background:#4a4a4a}
.footer-links{left:132px;top:230px;font-size:10.5px;color:#ddd}
.footer-links span{margin:0 6px;color:#888}
.copyright{left:132px;top:259px;font-size:10.5px;color:#ddd}
.badge{position:absolute;top:225px;height:36px;background:#8c8c8c}
.dot{position:absolute;top:232px;width:24px;height:24px;border-radius:50%}
</style>
</head>
<body>

<header class="site-header">
  <div class="abs brand-mark"></div>
  <div class="abs brand-name">Pine Gate Porch Realty</div>
  <div class="abs brand-rule"></div>
  <div class="abs brand-tag">REAL ESTATE TEAM</div>
  <div class="abs header-contact">
    <div><svg width="13" height="13" viewBox="0 0 24 24"><path fill="#333" d="M6.6 10.8a15 15 0 0 0 6.6 6.6l2.2-2.2c.3-.3.7-.4 1-.2 1.1.4 2.3.6 3.6.6.6 0 1 .4 1 1V20c0 .6-.4 1-1 1A17 17 0 0 1 3 4c0-.6.4-1 1-1h3.5c.6 0 1 .4 1 1 0 1.3.2 2.5.6 3.6.1.3 0 .7-.2 1z"/></svg>Phone Number: (555) 614-2970</div>
    <div><svg width="14" height="11" viewBox="0 0 24 18"><path fill="#333" d="M0 0h24v2L12 10 0 2zM0 4l12 8 12-8v14H0z"/></svg>Email: ReachOut@PineGatePorchRealty.example</div>
  </div>
</header>

<nav class="abs main-nav">
  <a class="active" href="#">Home</a><a href="#">About Us</a><a href="#">Buy</a><a href="#">Sell</a><a href="#">Rent</a><a href="#">Testimonials</a><a href="#">Blog</a><a href="#">Contact Us</a>
</nav>

<section class="abs hero" role="img" aria-label="Modern two-storey home with lit windows at dusk">
  <h1 class="abs hero-title">MAURIS PULVINAR VOLUTPAT</h1>
  <a class="abs btn btn-buy" href="#">BUY HOME</a>
  <a class="abs btn btn-sell" href="#">SELL MY HOME</a>
  <svg class="abs hero-arrow" style="left:36px" width="16" height="20" viewBox="0 0 16 20"><path d="M12 2 4 10l8 8" stroke="#fff" stroke-width="3" fill="none"/></svg>
  <svg class="abs hero-arrow" style="left:1148px" width="16" height="20" viewBox="0 0 16 20"><path d="m4 2 8 8-8 8" stroke="#fff" stroke-width="3" fill="none"/></svg>

  <form class="abs search-panel">
    <div class="search-head">SEARCH LISTINGS</div>
    <div class="field" style="left:20px;top:67px;width:316px">Property Type</div>
    <div class="field" style="left:20px;top:115px;width:316px"><svg width="9" height="12" viewBox="0 0 10 14" style="margin-right:8px"><path fill="#888" d="M5 0a5 5 0 0 0-5 5c0 4 5 9 5 9s5-5 5-9a5 5 0 0 0-5-5zm0 7a2 2 0 1 1 0-4 2 2 0 0 1 0 4z"/></svg>Enter Country, City or Zipcode</div>
    <div class="label" style="left:20px;top:170px">PRICE</div>
    <div class="field" style="left:20px;top:182px;width:150px">From<span class="caret"><svg width="10" height="6"><path d="M0 0h10L5 6z" fill="#555"/></svg></span></div>
    <div class="field" style="left:186px;top:182px;width:150px">To<span class="caret"><svg width="10" height="6"><path d="M0 0h10L5 6z" fill="#555"/></svg></span></div>
    <div class="label" style="left:20px;top:237px">BEDS</div>
    <div class="label" style="left:186px;top:237px">BATHS</div>
    <div class="field" style="left:20px;top:249px;width:150px">Any<span class="caret"><svg width="10" height="6"><path d="M0 0h10L5 6z" fill="#555"/></svg></span></div>
    <div class="field" style="left:186px;top:249px;width:150px">Any<span class="caret"><svg width="10" height="6"><path d="M0 0h10L5 6z" fill="#555"/></svg></span></div>
    <div class="abs search-btn">SEARCH</div>
    <a class="abs adv-link" href="#">ADVANCED SEARCH</a>
  </form>
</section>

<section>
  <h2 class="section-title" style="top:683px">Welcome</h2>
  <p class="abs welcome-text">Integer sapien felis, sodales ut lacus non, dignissim pretium nibh. Vivamus tempus quam et risus fringilla dignissim. Etiam rutrum justo cursus dolor laoreet, eu gravida leo ullamcorper. Pellentesque magna orci, placerat at nisl at, porta ultrices turpis. Fusce in eros non orci posuere viverra ut a lectus. In mattis, lorem sit amet consequat placerat, augue nulla mollis turpis, vitae egestas est tellus in nulla. Vestibulum convallis rutrum tincidunt. Aenean sit amet suscipit leo. Aenean commodo luctus ipsum, at pulvinar ipsum rutrum ut. Phasellus non volutpat eros. Pellentesque pharetra vehicula risus vitae sagittis.</p>
</section>
<div class="rule" style="top:888px"></div>

<section>
  <h2 class="section-title" style="top:958px">Listings</h2>
  <span class="mini-arrow" style="left:473px"><svg width="6" height="10"><path d="M5 1 1 5l4 4" stroke="#999" fill="none"/></svg></span>
  <span class="mini-arrow" style="left:703px"><svg width="6" height="10"><path d="m1 1 4 4-4 4" stroke="#999" fill="none"/></svg></span>
  <article class="listing" style="left:132px">
    <div class="photo" role="img" aria-label="Hillside house lit at dusk above a bay" style="background:linear-gradient(180deg,#1f5b9c,#3b7fc1 45%,#a4622e 70%,#5a4a8a)"></div>
    <h3>Nulla tristique posuere</h3>
    <div class="addr">24 Building name, street name, city - zipcode</div>
    <div class="price"><b>$00,000</b> - 4 Beds, 2 Baths</div>
  </article>
  <article class="listing" style="left:451px">
    <div class="photo" role="img" aria-label="Red brick family house with lawn" style="background:linear-gradient(180deg,#9cc0e4,#c3d6e8 35%,#a0533b 60%,#6f8f4c)"></div>
    <h3>Nulla tristique posuere</h3>
    <div class="addr">24 Building name, street name, city - zipcode</div>
    <div class="price"><b>$00,000</b> - 4 Beds, 2 Baths</div>
  </article>
  <article class="listing" style="left:770px">
    <div class="photo" role="img" aria-label="Modern villa with infinity pool" style="background:linear-gradient(180deg,#e4e4e2,#c9c2b8 45%,#6aa7c9 70%,#3d86b4)"></div>
    <h3>Nulla tristique posuere</h3>
    <div class="addr">24 Building name, street name, city - zipcode</div>
    <div class="price"><b>$00,000</b> - 4 Beds, 2 Baths</div>
  </article>
</section>

<section class="abs sell-band">
  <h2 class="abs sell-title">SELL HOME</h2>
  <p class="abs sell-text">Integer sapien felis, sodales ut lacus non, dignissim pretium nibh. Vivamus tempus quam et risus fringilla dignissim. Etiam rutrum justo cursus dolor laoreet, eu gravida leo ullamcorper. Pellentesque magna orci, placerat at nisl at, porta ultrices turpis. Fusce in eros non orci posuere viverra ut a lectus. In mattis, lorem sit amet consequat placerat, augue nulla mollis turpis, vitae egestas est tellus in nulla. Vestibulum convallis rutrum tincidunt. Aenean sit amet suscipit leo. Aenean commodo luctus ipsum, at pulvinar ipsum rutrum ut. Phasellus non volutpat eros. Pellentesque pharetra vehicula risus vitae sagittis.</p>
  <a class="abs btn-read" href="#">Read more</a>
  <div class="abs sell-photo" role="img" aria-label="Handshake over a desk with a small model house"></div>
</section>

<section class="abs testi">
  <h2 class="section-title" style="top:75px">Testimonials</h2>
  <p class="abs quote">“ Pellentesque blandit lacus eget nunc faucibus, et tincidunt eros viverra. Phasellus consequat sagittis nisi suscipit feugiat. Cras eget leo sed nunc hendrerit ultricies eu at nisl. Praesent iaculis faucibus urna sit amet lacinia. Maecenas consequat justo enim, ac mattis massa imperdiet quis. ”</p>
  <div class="abs author">- Dana Whitfield, City name</div>
  <svg class="abs" style="left:32px;top:150px" width="14" height="26" viewBox="0 0 14 26"><path d="M12 2 2 13l10 11" stroke="#999" stroke-width="2" fill="none"/></svg>
  <svg class="abs" style="left:1154px;top:150px" width="14" height="26" viewBox="0 0 14 26"><path d="m2 2 10 11L2 24" stroke="#999" stroke-width="2" fill="none"/></svg>
</section>

<section>
  <h2 class="abs blog-title">BLOG</h2>
  <a class="abs view-all" href="#">View All</a>
  <article class="post" style="left:132px">
    <div class="photo" role="img" aria-label="Stone manor house with a round garden" style="background:linear-gradient(180deg,#7fb0e0,#b89a6a 45%,#8b7a55 65%,#4f8a3a)"></div>
    <div class="post-body"><h3>Sed libero felis, vestibulum et dolor eget, lacinia aliquet neque.</h3><div class="date">9 August, 2017</div><p>Aliquam erat volutpat. Pellentesque blandit lacus eget nunc faucibus, et tincidunt eros viverra. Phasellus consequat sagittis nisi suscipit feugiat. Cras eget leo sed nunc hendrerit ultricies eu at nisl.</p><a class="more" href="#">READ MORE</a></div>
  </article>
  <article class="post" style="left:451px">
    <div class="photo" role="img" aria-label="White modern house under blue sky" style="background:linear-gradient(180deg,#4f8fd6,#dfe7ef 40%,#f2f2f2 65%,#a2584a)"></div>
    <div class="post-body"><h3>Sed libero felis, vestibulum et dolor eget, lacinia aliquet neque.</h3><div class="date">9 August, 2017</div><p>Aliquam erat volutpat. Pellentesque blandit lacus eget nunc faucibus, et tincidunt eros viverra. Phasellus consequat sagittis nisi suscipit feugiat. Cras eget leo sed nunc hendrerit ultricies eu at nisl.</p><a class="more" href="#">READ MORE</a></div>
  </article>
  <article class="post" style="left:770px">
    <div class="photo" role="img" aria-label="Family sitting on the lawn of a brick home" style="background:linear-gradient(180deg,#8fb8e6,#b39a86 45%,#c8b8a8 65%,#5e9a3d)"></div>
    <div class="post-body"><h3>Sed libero felis, vestibulum et dolor eget, lacinia aliquet neque.</h3><div class="date">9 August, 2017</div><p>Aliquam erat volutpat. Pellentesque blandit lacus eget nunc faucibus, et tincidunt eros viverra. Phasellus consequat sagittis nisi suscipit feugiat. Cras eget leo sed nunc hendrerit ultricies eu at nisl.</p><a class="more" href="#">READ MORE</a></div>
  </article>
</section>
<div class="rule" style="top:2756px"></div>

<section>
  <h2 class="section-title" style="top:2828px">Contact Info</h2>
  <div class="abs contact-box">
    <div class="contact-line" style="top:50px"><svg width="11" height="15" viewBox="0 0 10 14"><path fill="#777" d="M5 0a5 5 0 0 0-5 5c0 4 5 9 5 9s5-5 5-9a5 5 0 0 0-5-5zm0 7a2 2 0 1 1 0-4 2 2 0 0 1 0 4z"/></svg>24 Building name, Street name, City - Zipcode</div>
    <div class="contact-line" style="top:90px"><svg width="11" height="15" viewBox="0 0 10 14"><rect x="1.5" y="0.5" width="7" height="13" rx="1.5" fill="none" stroke="#777" stroke-width="1.6"/></svg>555 0193274</div>
    <div class="contact-line" style="top:130px"><svg width="13" height="10" viewBox="0 0 24 18"><path fill="#777" d="M0 0h24v2L12 10 0 2zM0 4l12 8 12-8v14H0z"/></svg>info@pinegateporchrealty.example</div>
    <span class="social-ring" style="left:34px"></span>
    <span class="social-ring" style="left:90px"></span>
    <span class="social-ring" style="left:146px"></span>
    <span class="social-ring" style="left:202px"></span>
  </div>
  <div class="abs map" role="img" aria-label="Road map of the surrounding area"></div>
</section>

<footer class="abs site-footer">
  <p class="abs legal" style="top:35px">Sunstate MLS Footnote Disclaimer : IDX information is provided exclusively for consumers' personal, noncommercial use, that it may not be used for any purpose other than to identify prospective properties consumers maybe interested in purchasing, and that the data is deemed reliable but is not guaranteed accurate by the MLS.</p>
  <p class="abs legal" style="top:100px">Listing information courtesy of Sunstate Regional Listing Service. All listing information is deemed reliable but not guaranteed and should be independently verified through personal inspection by appropriate professionals. Listings displayed on this website may be subject to prior sale or removal from sale; availability of any listing should always be independently verified. Listing information is provided for consumer personal, non-commercial use, solely to identify potential properties for potential purchase; all other use is strictly prohibited and may violate relevant federal and state law.</p>
  <div class="abs footer-rule"></div>
  <div class="abs footer-links">Home<span>|</span>About Us<span>|</span>Buy<span>|</span>Sell<span>|</span>Rent<span>|</span>Testimonials<span>|</span>Blog<span>|</span>Contact Us</div>
  <div class="abs copyright">Copyright © 2017 &nbsp;Pine Gate Porch Realty. &nbsp;&nbsp;All rights reserved.</div>
  <span class="badge" style="left:700px;width:96px"></span>
  <span class="badge" style="left:812px;width:32px"></span>
  <span class="badge" style="left:865px;width:38px"></span>
  <span class="dot" style="left:943px;background:#3b5a9a"></span>
  <span class="dot" style="left:976px;background:#1da1e2"></span>
  <span class="dot" style="left:1009px;background:#0a77b5"></span>
  <span class="dot" style="left:1042px;background:#dd4b39"></span>
</footer>

</body>
</html>
```